Flyer-Design für psychologisches Coaching  und Taiji
Flyer-Design für psychologisches Coaching und Taiji
Zielgruppe
Seit Januar 2020 habe ich mich selbständig gemacht und biete unter dem Namen 'WANDELRAUM - Mara Brenner, Coaching und Bewegung' Coaching sowie Taiji an. Der Corona-Lockdown hat meinen Geschäftseintritt stark beeinflusst, so dass ich für den Restart einen professionellen Flyer benötige, um mich und mein Angebot bekannt zu machen. Die Flyer werde ich vor meinen Räumen sowie in Geschäften im Umkreis und/oder per Einwurf verteilen.
Meine Zielgruppe sind gesundheitsorientierte Menschen in der zweiten Lebenshälfte, die ihre Balance finden wollen.
Mehr im separaten Dokument, bitte lesen.
Aufgabenstellung
Das Design soll zum Logo und zu meinem angestrebten Image passen. Ich möchte seriös, sympathisch und authentisch rüberkommen. Das psychologische Coaching und Taiji sollen gleichwertig und harmonisch präsentiert werden. Die Texte sollen kurz und prägnant sein. Textvorschläge gebe ich im Briefing und freue mich über neue, aussagefähige Formulierungen.
Mehr im beigefügten Dokument, bitte lesen.

```html
<!DOCTYPE html>
<html lang="de">
<head>
<meta charset="utf-8">
<title>Wandelraum – Flyer</title>
<link href="https://fonts.googleapis.com/css2?family=Quicksand:wght@400;500;600;700&family=Caveat:wght@400&display=swap" rel="stylesheet">
<style>
:root{
  --olive:#a89f3c;
  --olive-dark:#8f8730;
  --paper:#fbfaf5;
  --ink:#55534d;
  --ink-strong:#44423d;
  --stage:#e9e9e7;
  --rule:#ebe8dc;
  --row:#f1efe4;
  --signature:#4f5d8a;
}
*{box-sizing:border-box;margin:0;padding:0}
html,body{width:1200px;height:1200px;overflow:hidden}
body{background:var(--stage);font-family:"Quicksand",sans-serif;color:var(--ink);position:relative}

.sheet{position:absolute;display:flex;background:var(--paper);box-shadow:0 2px 10px rgba(0,0,0,.08);overflow:hidden}
.sheet--dl{left:20px;top:392px;width:392px;height:416px}
.sheet--outside{left:430px;top:40px;width:750px;height:530px}
.sheet--inside{left:430px;top:620px;width:750px;height:530px}

.panel{position:relative;width:250px;height:100%;padding:24px 18px 0;overflow:hidden}
.sheet--dl .panel{width:196px;padding:16px 14px 0}
.panel + .panel{border-left:1px solid var(--rule)}
.band{position:absolute;left:0;right:0;bottom:0;height:40px;background:var(--olive)}

h2{font-weight:500;color:var(--olive);font-size:10px;letter-spacing:.12em;text-transform:uppercase;margin-bottom:12px;position:relative}
h3{font-weight:500;color:var(--olive);font-size:7.8px;margin:11px 0 4px;position:relative}
p,li{font-size:6.6px;line-height:1.45;position:relative}
p + p{margin-top:3px}
b{font-weight:700;color:var(--ink-strong)}
ul{list-style:none;position:relative}
li::before{content:"• "}
li{margin-bottom:2px}

.brand{display:flex;flex-direction:column;align-items:center;gap:7px;position:relative}
.brand__mark{width:30px;height:30px;border-radius:50%;background:var(--olive)}
.brand__name{font-weight:600;color:var(--olive);font-size:13px;letter-spacing:.06em}

.photo{position:absolute;border:3px solid #fff;box-shadow:0 1px 3px rgba(0,0,0,.18)}
.glow{position:absolute;left:0;right:0;background:linear-gradient(180deg,rgba(168,159,60,0) 0%,rgba(168,159,60,.35) 100%)}
.glow--top{top:0;height:150px;background:linear-gradient(0deg,rgba(168,159,60,0) 0%,rgba(168,159,60,.4) 100%)}

.contact{font-size:6.4px;color:var(--olive);text-align:center;line-height:1.6;position:relative}
.contact__title{font-weight:700;font-size:7.4px;letter-spacing:.06em;margin-bottom:4px}
.contact__cols{display:flex;justify-content:center;gap:7px;margin-top:3px}
.contact__cols span:first-child{text-align:right}
.contact__cols span + span{border-left:1px solid var(--olive);padding-left:7px;text-align:left}
.contact__web{margin-top:5px;font-size:7px}
.signature{font-family:"Caveat",cursive;color:var(--signature);font-size:13px;text-align:center;line-height:1.2;margin-top:12px}

.cover{background:linear-gradient(180deg,#eeede6 0%,#efe9d4 45%,#f3d7b5 70%,#c7b775 85%,#a8a44a 100%);padding-top:16px}
.cover__logo{background:var(--paper);margin:0 auto;width:134px;padding:12px 0}
.cover__logo .brand__mark{width:24px;height:24px}
.cover__logo .brand__name{font-size:11px}
.cover__title{margin-top:36px;text-align:center;font-weight:400;color:var(--olive-dark);font-size:15px;line-height:1.4;text-transform:uppercase}
.cover__sub{text-align:center;margin-top:16px;font-weight:600;color:var(--olive);font-size:7.4px;letter-spacing:.03em}
.cover__art{position:absolute;left:0;right:0;top:220px;bottom:0;background:linear-gradient(180deg,rgba(244,217,140,0) 0%,rgba(241,182,163,.55) 45%,rgba(168,164,74,.9) 85%)}
.sheet--dl .cover__logo{width:112px;padding:10px 0}
.sheet--dl .cover__title{font-size:12.5px;margin-top:28px}
.sheet--dl .cover__sub{font-size:6.2px;margin-top:12px}
.sheet--dl .cover__art{top:190px}

.schedule h2{font-size:8.4px;letter-spacing:.03em;margin:12px 0 5px}
.schedule h3{font-size:5.8px;font-weight:600;margin:0 0 4px}
.schedule h4{font-size:5.6px;font-weight:700;color:var(--ink-strong);margin:7px 0 3px}
.schedule p{font-size:5.4px;line-height:1.4}
.schedule .brand{gap:4px}
.schedule .brand__mark{width:20px;height:20px}
.schedule .brand__name{font-size:8px}
.dates{width:100%;border-collapse:collapse;font-size:5.2px}
.dates td{padding:0.6px 2px;line-height:1.25}
.dates tr:nth-child(odd){background:var(--row)}
.dates td:last-child{text-align:right}
.dl-contact{background:var(--paper);border-top:1px solid var(--rule);margin-top:8px;padding-top:6px;font-size:5.4px}
.dl-contact .contact__title{font-size:6.2px}
.dl-contact .contact__web{font-size:5.8px}
.dl-band{position:absolute;left:0;right:0;bottom:0;height:12px;background:var(--olive)}

.intro{margin-top:160px}
.lead{font-size:7.4px;color:var(--olive);text-align:center;margin-top:12px;line-height:1.5}
.services{text-align:center}
.services h4{font-weight:500;color:var(--olive);font-size:8.8px;letter-spacing:.12em;margin:12px 0 2px}
.services p{font-size:6.6px}
</style>
</head>
<body>

<section class="sheet sheet--dl" aria-label="DL-Flyer">
  <article class="panel cover">
    <div class="cover__logo brand">
      <div class="brand__mark"></div>
      <div class="brand__name">WANDELRAUM</div>
    </div>
    <h1 class="cover__title">Zu sich selbst<br>finden und zur<br>Ruhe kommen</h1>
    <div class="cover__sub">COACHING, TAIJI, QIGONG, MEDITATION</div>
    <div class="cover__art" role="img" aria-label="Illustration: Frau mit ausgebreiteten Armen auf einer Wiese im Sonnenuntergang"></div>
  </article>

  <article class="panel schedule">
    <div class="brand">
      <div class="brand__mark"></div>
      <div class="brand__name">WANDELRAUM</div>
    </div>
    <h2>AKTUELLE TERMINE IM SOMMER 2020</h2>
    <h3>Kostenlose Schnupperstunde Taiji, Qigong und Meditation</h3>
    <p>Eine Schnupperstunde dauert 75 min und beinhaltet einen Mix aus Taiji, Qigong und Meditation. So können Sie es zuerst ausprobieren, bevor Sie in einen laufenden Kurs einsteigen. Bitte seien sie mindestens 10 min vor Beginn der Stunde da, um sich entsprechend einstimmen zu können. Tragen Sie bequeme Sportkleidung und warme Socken oder Taiji-Schuhe. Auch Stoppersocken oder Barfußschuhe sind okay.</p>
    <h4>Die nächsten kostenlosen Schnupperstunden:</h4>
    <table class="dates">
      <tr><td>Mittwoch</td><td>01. Juli 2020</td><td>18:30 Uhr bis 19:45 Uhr</td></tr>
      <tr><td>Mittwoch</td><td>08. Juli 2020</td><td>18:30 Uhr bis 19:45 Uhr</td></tr>
      <tr><td>Donnerstag</td><td>16. Juli 2020</td><td>19:45 Uhr bis 21:00 Uhr</td></tr>
      <tr><td>Montag</td><td>20. Juli 2020</td><td>20:00 Uhr bis 21:15 Uhr</td></tr>
      <tr><td>Mittwoch</td><td>29. Juli 2020</td><td>19:00 Uhr bis 20:15 Uhr</td></tr>
      <tr><td>Donnerstag</td><td>06. August 2020</td><td>19:30 Uhr bis 20:45 Uhr</td></tr>
      <tr><td>Montag</td><td>10. August 2020</td><td>20:00 Uhr bis 21:15 Uhr</td></tr>
      <tr><td>Mittwoch</td><td>19. August 2020</td><td>19:00 Uhr bis 20:15 Uhr</td></tr>
      <tr><td>Freitag</td><td>28. August 2020</td><td>19:00 Uhr bis 20:15 Uhr</td></tr>
    </table>
    <h3 style="margin-top:8px">Offener Meditationsabend</h3>
    <p>Einmal im Monat lade ich zu einem offenen Meditationsabend ein. Sie sind herzlich willkommen, ganz unabhängig von Ihrer Meditationserfahrung. Ich biete verschiedene Übungen ohne religiöse oder spirituelle Bindung an und freue mich über einen freiwilligen Kostenbeitrag.</p>
    <h4>Nächste offene Meditationsabende:</h4>
    <table class="dates">
      <tr><td>Freitag</td><td>24. Juli 2020</td><td>19:00 Uhr bis 20:15 Uhr</td></tr>
      <tr><td>Mittwoch</td><td>26. August 2020</td><td>19:30 Uhr bis 20:45 Uhr</td></tr>
    </table>
    <div class="contact dl-contact">
      <div class="contact__title">KONTAKT:</div>
      <div>Wandelraum · Mara Brenner · Coaching und Bewegung</div>
      <div class="contact__cols">
        <span>Lindenweg 9<br>61350 Talheim</span>
        <span>info@wandelraum-coaching.de<br>mobil: 0151 4062297</span>
      </div>
      <div class="contact__web">www.wandelraum-coaching.de</div>
    </div>
    <div class="dl-band"></div>
  </article>
</section>

<section class="sheet sheet--outside" aria-label="Faltflyer Außenseite">
  <article class="panel">
    <h2>Meditation</h2>
    <p>Kennen Sie das? Sie haben noch 1000 Dinge auf Ihrer to-do-Liste und wissen nicht, wo Ihnen der Kopf steht. Außerdem haben Sie gerade eine schwierige Phase in der Firma. Und schon länger diesen Stress in Ihrer Familie. Und Sie wissen, dass Sie endlich mal was für sich tun sollten. Aber wann denn bloß?</p>
    <p>Für mehr und mehr Menschen ist es wichtig geworden, im hektischen Alltag Inseln der Ruhe zu schaffen.</p>
    <h3>Offene Meditationsabende</h3>
    <p>Falls Sie es ausprobieren möchten oder eine regelmäßige Meditationsgruppe suchen, kommen Sie doch einfach zu einem meiner offenen Meditationsabende. Jede/r ist herzlich eingeladen, unabhängig von der Vorerfahrung mit Meditation.</p>
    <p>Wir erkunden unter meiner Anleitung Techniken aus verschiedenen Meditationspraktiken – frei von religiöser oder spiritueller Bindung.</p>
    <p>Diese Abende biete ich auf der Basis freiwilliger Kostenbeteiligung an. Die Termine finden Sie auf meiner Website.</p>
    <div class="glow" role="img" aria-label="Dekorativer Pinselschwung in Oliv" style="top:320px;bottom:40px"></div>
    <div class="band"></div>
    <div class="photo" role="img" aria-label="Foto: Trainerin im Meditationssitz mit Kerze" style="left:112px;top:320px;width:128px;height:172px;background:linear-gradient(180deg,#8fa5a8,#6d6f7a 55%,#c9c7c4)"></div>
  </article>

  <article class="panel">
    <div class="brand" style="margin-top:14px">
      <div class="brand__mark" style="width:34px;height:34px"></div>
      <div class="brand__name" style="font-size:14px">WANDELRAUM</div>
    </div>
    <div class="contact" style="margin-top:24px">
      <div class="contact__title">KONTAKT:</div>
      <div>Wandelraum · Mara Brenner · Coaching und Bewegung</div>
      <div class="contact__cols">
        <span>Lindenweg 9<br>61350 Talheim</span>
        <span>info@wandelraum-coaching.de<br>mobil: 0151 4062297</span>
      </div>
      <div class="contact__web">www.wandelraum-coaching.de</div>
    </div>
    <p style="margin-top:30px">Die Räumlichkeiten befinden sich in der Innenstadt Talheims. Auf der Grundfläche von ca. 75 m² finden die Kurse und Coachings statt.</p>
    <div class="signature">Ich freue mich auf Sie!<br>Mara Brenner</div>
    <div class="glow" style="top:350px;bottom:40px"></div>
    <div class="band"></div>
    <div class="photo" role="img" aria-label="Foto: Kursraum mit Wandbild und Meditationskissen" style="left:8px;top:368px;width:234px;height:128px;background:linear-gradient(180deg,#e9e6df 0%,#d9d3c8 45%,#b98a5a 100%)"></div>
  </article>

  <article class="panel cover">
    <div class="cover__logo brand">
      <div class="brand__mark"></div>
      <div class="brand__name">WANDELRAUM</div>
    </div>
    <h1 class="cover__title">Zu sich selbst<br>finden und zur<br>Ruhe kommen</h1>
    <div class="cover__sub">COACHING, TAIJI, QIGONG, MEDITATION</div>
    <div class="cover__art" role="img" aria-label="Illustration: Frau mit ausgebreiteten Armen auf einer Wiese im Sonnenuntergang"></div>
  </article>
</section>

<section class="sheet sheet--inside" aria-label="Faltflyer Innenseite">
  <article class="panel">
    <div class="glow glow--top" role="img" aria-label="Dekorativer Pinselschwung in Oliv"></div>
    <p class="intro">Die Angebote von „WANDELRAUM – Mara Brenner“ helfen Ihnen dabei, <b>sich neu auszurichten, zur Ruhe zu kommen und zu sich selbst zu finden.</b> Dabei lege ich Wert auf die Verbindung von <b>Geist, Körper und Seele</b> und setze dafür gezielt körperorientierte Methoden und die Lenkung der Aufmerksamkeit (des inneren Fokus) ein.</p>
    <div class="lead">Bei mir finden Sie Coaching und Bewegung,<br>im Einzelnen heißt das:</div>
    <div class="services">
      <h4>PSYCHOLOGISCHES COACHING</h4>
      <p>ich begleite Sie in schwierigen Lebensphasen mit körperorientierten Methoden</p>
      <h4>TAIJI UND QIGONG</h4>
      <p>erleben Sie sich mit langsamen Bewegungen im Fluss</p>
      <h4>MEDITATION</h4>
      <p>richten Sie den Fokus ganz nach innen und…<br>einfach nur sein</p>
    </div>
    <div class="band"></div>
  </article>

  <article class="panel">
    <h2>Psychologisches Coaching</h2>
    <p>Wünschen Sie sich <b>Begleitung</b> in Situationen, die Sie selbst als schwierig empfinden? Ich biete Ihnen:</p>
    <ul style="margin-top:7px">
      <li><b>Hilfe zur Selbsthilfe</b>, z.B. in persönlichen Krisensituationen (Trennung, Konflikte, Ängste)</li>
      <li><b>Neuorientierung</b>, beruflich und privat, unter Berücksichtigung Ihrer individuellen Stärken und Bedürfnisse</li>
      <li>Methoden und Ansätze zur <b>Stressbewältigung</b>, um sich vor Erschöpfung und Burn-out zu schützen</li>
      <li>Meine eigene <b>Lebens- und Berufserfahrung</b> als Führungskraft mit zahlreichen einschneidenden Veränderungen sowie einen umfangreichen <b>Methoden-Fundus</b></li>
    </ul>
    <h3>Ihr nachhaltiger Nutzen:</h3>
    <ul>
      <li><b>erweiterte Handlungsmöglichkeiten</b></li>
      <li><b>veränderte Einstellung</b>, die Ihnen mehr Spielraum gibt</li>
      <li><b>neue Möglichkeiten</b>, schwierige Situationen zu meistern</li>
      <li><b>Sie sehen klarer</b>, wer Sie sind und was Sie wollen</li>
    </ul>
    <h3>Gerne bin ich für Sie da.</h3>
    <p>Vereinbaren Sie unverbindlich ein kostenloses Erstgespräch mit mir entweder per Mail unter <b>info@wandelraum-coaching.de</b> oder telefonisch unter <b>0151 4062297</b>.</p>
    <div class="band"></div>
    <div class="photo" role="img" aria-label="Porträtfoto der Coachin vor rotem Hintergrund" style="left:28px;top:406px;width:194px;height:86px;border:none;background:linear-gradient(90deg,#7e2a2a,#a8413b 50%,#7e2a2a)"></div>
  </article>

  <article class="panel">
    <h2>Taiji und Qigong</h2>
    <p>Taiji und Qigong sind <b>langsame und fließende Bewegungen.</b> Beides stammt aus den Kampfkünsten im alten China und dient der <b>Gesundheitsförderung.</b> Ich unterrichte nach der Tradition der Familie Wen. Die Teilnehmenden richten ihre Aufmerksamkeit nach innen bzw. ganz auf die Bewegungen. Der <b>meditative Aspekt</b> steht für mich klar im Vordergrund.</p>
    <h3>Möglicher Nutzen für Sie:</h3>
    <ul>
      <li>Mehr <b>Ruhe und Gelassenheit</b> im Alltag</li>
      <li>Schulung der <b>Konzentration</b></li>
      <li>Verbesserung der <b>Körperwahrnehmung</b></li>
      <li><b>Kräftigung</b> der Sehnen und Gelenke</li>
      <li>Aufrechtere <b>Körperhaltung</b></li>
    </ul>
    <h3>Wie können Sie einsteigen?</h3>
    <p>Bitte besuchen Sie immer zuerst eine <b>kostenlose Schnupperstunde</b> bei mir, um Taiji und Qigong einfach mal auszuprobieren. Wann die nächsten Schnupperstunden stattfinden, sehen sie auf meiner Website.</p>
    <div class="glow" role="img" aria-label="Dekorativer Pinselschwung in Oliv" style="top:310px;bottom:40px"></div>
    <div class="band"></div>
    <div class="photo" role="img" aria-label="Foto: Trainerin in einer Taiji-Haltung mit erhobenen Armen" style="left:22px;top:318px;width:122px;height:176px;background:linear-gradient(180deg,#9fb2b7,#7a7b86 50%,#d6d2c9)"></div>
  </article>
</section>

</body>
</html>
```